Orrin Funeral Home stationery
Orrin Funeral Home
Professional
Duncan P. Orrin
Funeral Director
41 Larch St.
Wrenford, VT 04682
and
58 Mill St.
Dunmere, VT 04657
207-516-2870 or 207-739-6152
duncan@orrinfuneralhome.example
www.orrinfuneralhome.example
The Eastport address is the 739 phone number
Logo
Funerals - Cremations - Prearrangements
Logo in eps

```html
<!DOCTYPE html>
<html lang="en">
<head>
<meta charset="utf-8">
<title>Orrin Funeral Home stationery</title>
<link rel="stylesheet" href="https://fonts.googleapis.com/css2?family=Cinzel:wght@400;600&display=swap">
<style>
:root{
  --navy:#0b1c66;
  --blue:#1f3f9e;
  --gold:#b38b52;
  --paper:#ffffff;
  --stage:#ffffff;
  --edge:#d8dbe3;
  --ink:#1b2a74;
  --light:#ffffff;
}
*{margin:0;padding:0;box-sizing:border-box}
html,body{width:1200px;height:763px;overflow:hidden;background:var(--stage)}
body{position:relative;font-family:"Cinzel",serif;color:var(--ink)}
.sheet{position:absolute;background:var(--paper);border:1px solid var(--edge);overflow:hidden;box-shadow:0 1px 3px rgba(0,0,0,.12)}
.band{position:absolute;left:0;right:0;bottom:0}
.band svg{position:absolute;inset:0;width:100%;height:100%}
.band-text{position:absolute;color:var(--light);line-height:1.5;letter-spacing:.02em;white-space:nowrap}
.brand{position:absolute;display:flex;align-items:center;gap:6px;color:var(--ink);font-weight:600;white-space:nowrap}
.brand .mark{background:var(--ink);flex:none}
.brand.on-blue{color:var(--light)}
.brand.on-blue .mark{background:var(--light)}

/* letterhead */
.letterhead{left:19px;top:24px;width:538px;height:710px}
.letterhead .brand{left:26px;top:62px;font-size:24px}
.letterhead .brand .mark{width:16px;height:16px}
.letterhead .band{height:92px}
.letterhead .band-text{left:26px;top:40px;font-size:8px}

/* business card front */
.card-front{left:566px;top:60px;width:202px;height:120px}
.card-front .brand{left:9px;top:12px;font-size:8.5px;gap:4px}
.card-front .brand .mark{width:7px;height:7px}
.card-front .person{position:absolute;right:9px;top:8px;text-align:right;font-size:6.5px;font-weight:600}
.card-front .person span{display:block;font-size:4.5px;font-weight:400}
.card-front .details{position:absolute;left:10px;top:34px;font-size:4.6px;line-height:1.5;white-space:nowrap}
.card-front .band{height:32px}

/* card back, light */
.card-light{left:684px;top:199px;width:223px;height:130px}
.card-light .brand{left:14px;top:28px;font-size:10px;gap:5px}
.card-light .brand .mark{width:9px;height:9px}
.card-light .band{height:44px}
.card-light .band-text{left:12px;top:25px;font-size:5px}

/* card back, blue */
.card-blue{left:914px;top:252px;width:221px;height:132px;background:linear-gradient(160deg,var(--blue),var(--navy));border:none}
.card-blue .brand{left:50%;top:44px;transform:translateX(-50%);font-size:11px;gap:5px}
.card-blue .brand .mark{width:9px;height:9px}
.card-blue .tagline{position:absolute;left:0;right:0;top:78px;text-align:center;color:var(--light);font-size:5px;letter-spacing:.04em}

/* envelope */
.envelope{left:566px;top:396px;width:605px;height:341px}
.envelope .flap{position:absolute;left:0;top:0;width:100%;height:96px}
.envelope .flap svg{width:100%;height:100%}
.envelope .flap .brand{left:50%;top:30px;transform:translateX(-50%);font-size:13px}
.envelope .flap .brand .mark{width:10px;height:10px}
.envelope .body-brand{left:14px;top:128px;font-size:22px}
.envelope .body-brand .mark{width:15px;height:15px}
.envelope .band{height:80px}
.envelope .band-text{left:14px;top:30px;font-size:7.5px}
</style>
</head>
<body>

<section class="sheet letterhead" aria-label="Letterhead">
  <div class="brand"><span class="mark"></span>Orrin Funeral Home</div>
  <footer class="band">
    <svg viewBox="0 0 538 92" preserveAspectRatio="none" aria-hidden="true">
      <defs><linearGradient id="lhBlue" x1="0" y1="0" x2="1" y2="1"><stop offset="0" stop-color="#1f3f9e"/><stop offset="1" stop-color="#0b1c66"/></linearGradient></defs>
      <path d="M0 22 Q270 8 538 16 L538 92 L0 92 Z" fill="url(#lhBlue)"/>
      <path d="M0 18 Q270 4 538 12" stroke="#b38b52" stroke-width="3" fill="none"/>
    </svg>
    <p class="band-text">41 Larch St. Wrenford, VT 04682 and 58 Mill St. Dunmere, VT 04657<br>
    Phone: 207-516-2870 or 207-739-6152 | Fax: 207-516-2894<br>
    Email: duncan@orrinfuneralhome.example | www.orrinfuneralhome.example</p>
  </footer>
</section>

<section class="sheet card-front" aria-label="Business card front">
  <div class="brand"><span class="mark"></span>Orrin Funeral Home</div>
  <p class="person">Duncan P. Orrin<span>Funeral Director</span></p>
  <p class="details">41 Larch St. Wrenford, VT 04682<br>
  and 58 Mill St. Dunmere, VT 04657<br>
  Phone: 207-516-2870 or 207-739-6152<br>
  Fax: 207-516-2894<br>
  duncan@orrinfuneralhome.example<br>
  www.orrinfuneralhome.example</p>
  <div class="band">
    <svg viewBox="0 0 202 32" preserveAspectRatio="none" aria-hidden="true">
      <path d="M0 11 Q100 3 202 7 L202 32 L0 32 Z" fill="#13288a"/>
      <path d="M0 9 Q100 1 202 5" stroke="#b38b52" stroke-width="1.5" fill="none"/>
    </svg>
  </div>
</section>

<section class="sheet card-light" aria-label="Business card back">
  <div class="brand"><span class="mark"></span>Orrin Funeral Home</div>
  <div class="band">
    <svg viewBox="0 0 223 44" preserveAspectRatio="none" aria-hidden="true">
      <path d="M0 14 Q110 4 223 9 L223 44 L0 44 Z" fill="#13288a"/>
      <path d="M0 12 Q110 2 223 7" stroke="#b38b52" stroke-width="1.6" fill="none"/>
    </svg>
    <p class="band-text">Funerals - Cremations - Prearrangements</p>
  </div>
</section>

<section class="sheet card-blue" aria-label="Business card back, blue">
  <div class="brand on-blue"><span class="mark"></span>Orrin Funeral Home</div>
  <p class="tagline">Funerals - Cremations - Prearrangements</p>
</section>

<section class="sheet envelope" aria-label="Envelope">
  <div class="flap">
    <svg viewBox="0 0 605 96" preserveAspectRatio="none" aria-hidden="true">
      <defs><linearGradient id="flapBlue" x1="0" y1="0" x2="0" y2="1"><stop offset="0" stop-color="#1f3f9e"/><stop offset="1" stop-color="#0b1c66"/></linearGradient></defs>
      <path d="M0 0 H605 V56 Q302 106 0 56 Z" fill="url(#flapBlue)"/>
    </svg>
    <div class="brand on-blue"><span class="mark"></span>Orrin Funeral Home</div>
  </div>
  <div class="brand body-brand"><span class="mark"></span>Orrin Funeral Home</div>
  <footer class="band">
    <svg viewBox="0 0 605 80" preserveAspectRatio="none" aria-hidden="true">
      <defs><linearGradient id="envBlue" x1="0" y1="0" x2="1" y2="1"><stop offset="0" stop-color="#1f3f9e"/><stop offset="1" stop-color="#0b1c66"/></linearGradient></defs>
      <path d="M0 22 Q302 6 605 12 L605 80 L0 80 Z" fill="url(#envBlue)"/>
      <path d="M0 18 Q302 2 605 8" stroke="#b38b52" stroke-width="3" fill="none"/>
    </svg>
    <p class="band-text">41 Larch St. Wrenford,<br>VT 04682 and 58 Mill St.<br>Dunmere, VT 04657</p>
  </footer>
</section>

</body>
</html>
```